TIDAL VERGE needs bisness cards pronto

Bisness name is "TIDAL VERGE" new bisness the bisness includes lawn mowing, garden matanace, and any jobs around the house.
I need a card that is colorful and vibrant and the bisness of lawn mowing maybe with some nature with it. It also needs my contact details"Darren Quellby mobile 0413562049 call for free quote and email norma.vance@fernmail.com.au and a catchy tag line

Industry/Entity Type

House

Requirements
Must have
• Bisness name "TIDAL VERGE"
Contact details "0413562049"
Email norma.vance@fernmail.com.au
Call for free quote

```html
<!DOCTYPE html>
<html lang="en">
<head>
<meta charset="utf-8">
<title>Tidal Verge – Business Cards</title>
<link rel="stylesheet" href="https://fonts.googleapis.com/css2?family=Mulish:wght@400;700&display=swap">
<style>
  :root {
    --olive: #78781f;
    --olive-dark: #5f6116;
    --grass-light: #c9c46a;
    --grass-mid: #8f9a34;
    --grass-dark: #5d6a1e;
    --paper: #ffffff;
    --backdrop: #e3e7ea;
  }
  * { margin: 0; padding: 0; box-sizing: border-box; }
  html, body {
    width: 1200px; height: 1000px; overflow: hidden;
    background: var(--backdrop);
    font-family: "Mulish", Arial, sans-serif;
  }
  .sheet {
    position: relative; width: 1200px; height: 1000px;
    display: flex; flex-direction: column; align-items: center; justify-content: center; gap: 56px;
  }
  .card {
    position: relative; width: 760px; height: 434px;
    border-radius: 44px; overflow: hidden;
    box-shadow: 0 10px 28px rgba(40, 50, 60, 0.22);
  }
  .card-art { position: absolute; inset: 0; width: 100%; height: 100%; display: block; }

  .contact { position: absolute; left: 30px; top: 196px; color: var(--olive); font-weight: 700; font-size: 19px; line-height: 30px; }
  .cta { position: absolute; left: 72px; top: 322px; color: var(--olive); font-weight: 700; font-size: 27px; }

  .business-name {
    position: absolute; color: var(--paper);
    font-weight: 400; font-size: 30px; line-height: 1; white-space: nowrap;
  }
  .card-front .business-name { left: 420px; top: 218px; }
  .card-back .business-name { left: 0; right: 0; top: 124px; text-align: center; }
</style>
</head>
<body>
<main class="sheet">

  <section class="card card-front">
    <svg class="card-art" viewBox="0 0 760 434">
      <defs>
        <radialGradient id="lawnFront" cx="50%" cy="45%" r="55%">
          <stop offset="0" stop-color="var(--grass-light)"/>
          <stop offset="0.6" stop-color="var(--grass-mid)"/>
          <stop offset="1" stop-color="var(--grass-dark)"/>
        </radialGradient>
        <filter id="lawnEdge" x="-20%" y="-20%" width="140%" height="140%">
          <feGaussianBlur stdDeviation="4"/>
        </filter>
      </defs>
      <rect class="card-base" width="760" height="434" fill="var(--olive)"/>
      <rect class="card-panel" x="24" y="24" width="640" height="366" rx="40" fill="var(--paper)"/>
      <circle cx="596" cy="186" r="206" fill="rgba(60,60,20,0.35)" filter="url(#lawnEdge)"/>
      <circle class="lawn-photo" cx="590" cy="180" r="200" fill="url(#lawnFront)" role="img" aria-label="Close-up photograph of fresh green lawn grass"/>
    </svg>
    <p class="contact">Tel: 0413562049<br>Email:norma.vance@fernmail.com.au</p>
    <p class="cta">Call for free quote</p>
    <p class="business-name">TIDAL VERGE</p>
  </section>

  <section class="card card-back">
    <svg class="card-art" viewBox="0 0 760 434">
      <defs>
        <radialGradient id="lawnBack" cx="50%" cy="30%" r="70%">
          <stop offset="0" stop-color="var(--grass-light)"/>
          <stop offset="0.55" stop-color="var(--grass-mid)"/>
          <stop offset="1" stop-color="var(--grass-dark)"/>
        </radialGradient>
        <clipPath id="backFrame"><rect x="18" y="18" width="724" height="398" rx="36"/></clipPath>
        <filter id="domeEdge" x="-20%" y="-20%" width="140%" height="140%">
          <feGaussianBlur stdDeviation="5"/>
        </filter>
      </defs>
      <rect class="card-base" width="760" height="434" fill="var(--olive)"/>
      <g clip-path="url(#backFrame)">
        <ellipse cx="395" cy="470" rx="370" ry="300" fill="var(--olive-dark)" filter="url(#domeEdge)"/>
        <ellipse class="lawn-photo" cx="395" cy="476" rx="362" ry="292" fill="url(#lawnBack)" role="img" aria-label="Dome of fresh green lawn grass rising from the card edge"/>
      </g>
      <rect class="card-frame" x="18" y="18" width="724" height="398" rx="36" fill="none" stroke="var(--paper)" stroke-width="1.6"/>
    </svg>
    <p class="business-name">TIDAL VERGE</p>
  </section>

</main>
</body>
</html>
```